81M business card

I need a business card for a life sciences consulting firm I started. The company name is 81M and the logo is attached. I am looking for something edgey and current but different from the blah standard business card.

Industry/Entity Type

Business

Requirements
Nice to have
• Both sides

```html
<!DOCTYPE html>
<html lang="en">
<head>
<meta charset="utf-8">
<title>81M LLC Business Card</title>
<link rel="stylesheet" href="https://fonts.googleapis.com/css2?family=Arimo:wght@400;700&family=Tinos:wght@700&display=swap">
<style>
  :root {
    --frame-red: #d8101a;
    --card-white: #ffffff;
    --card-edge: #d9d9d9;
    --blue-deep: #0b1f5c;
    --blue-bright: #0a3db4;
    --orange-light: #ff9d3f;
    --orange-dark: #ff6510;
    --brand-blue: #1b3d8c;
    --tagline-grey: #6d6d6d;
    --text-light: #ffffff;
  }
  * { margin: 0; padding: 0; box-sizing: border-box; }
  html, body {
    width: 1200px;
    height: 693px;
    overflow: hidden;
    background: var(--card-white);
  }
  .canvas {
    position: relative;
    width: 1200px;
    height: 693px;
    background: var(--card-white);
  }
  .presentation-frame {
    position: absolute;
    left: 18px;
    top: 18px;
    width: 1164px;
    height: 655px;
    border: 4px solid var(--frame-red);
  }
  .card {
    position: absolute;
    left: 44px;
    top: 44px;
    width: 1112px;
    height: 602px;
    border: 1px solid var(--card-edge);
    overflow: hidden;
    background: var(--card-white);
    font-family: "Arimo", Arial, sans-serif;
  }
  .card-art {
    position: absolute;
    inset: 0;
    width: 1112px;
    height: 602px;
  }
  .brand-dot {
    position: absolute;
    left: 31px;
    top: 232px;
    width: 126px;
    height: 126px;
    border-radius: 50%;
    background: var(--orange-dark);
  }
  .brand-name {
    position: absolute;
    left: 188px;
    top: 258px;
    font-weight: 700;
    font-size: 60px;
    line-height: 1;
    letter-spacing: 2px;
    color: var(--brand-blue);
    white-space: nowrap;
  }
  .brand-tagline {
    position: absolute;
    left: 190px;
    top: 330px;
    font-size: 13.5px;
    letter-spacing: 0.3px;
    color: var(--tagline-grey);
    white-space: nowrap;
  }
  .identity {
    position: absolute;
    left: 646px;
    width: 400px;
    top: 124px;
    text-align: center;
    color: var(--text-light);
  }
  .identity-name {
    font-family: "Tinos", "Times New Roman", serif;
    font-weight: 700;
    font-size: 50px;
    line-height: 1;
    letter-spacing: 1px;
  }
  .identity-position {
    font-weight: 700;
    font-size: 23px;
    margin-top: 2px;
  }
  .contact {
    position: absolute;
    left: 706px;
    top: 410px;
    list-style: none;
    color: var(--text-light);
  }
  .contact-item {
    display: flex;
    align-items: center;
    gap: 24px;
    font-weight: 700;
    font-size: 23px;
    height: 37px;
  }
  .contact-icon {
    width: 20px;
    height: 30px;
    flex: none;
  }
</style>
</head>
<body>
<div class="canvas">
  <div class="presentation-frame"></div>
  <section class="card">
    <svg class="card-art" viewBox="0 0 1112 602" aria-hidden="true">
      <defs>
        <radialGradient id="blue-field" cx="690" cy="300" r="520" gradientUnits="userSpaceOnUse">
          <stop offset="0" stop-color="var(--blue-bright)"/>
          <stop offset="1" stop-color="var(--blue-deep)"/>
        </radialGradient>
        <linearGradient id="orange-band" x1="0" y1="0" x2="0" y2="602" gradientUnits="userSpaceOnUse">
          <stop offset="0" stop-color="var(--orange-light)"/>
          <stop offset="1" stop-color="var(--orange-dark)"/>
        </linearGradient>
      </defs>
      <polygon class="blue-field" points="353,0 1112,0 1112,602 330,602 643,286" fill="url(#blue-field)"/>
      <polygon class="orange-chevron" points="303,0 338,0 614,286 310,602 275,602 580,286" fill="url(#orange-band)"/>
    </svg>

    <span class="brand-dot"></span>
    <span class="brand-name">81M LLC</span>
    <p class="brand-tagline">life science advisory and project support</p>

    <div class="identity">
      <h1 class="identity-name">YOURNAME</h1>
      <p class="identity-position">Position</p>
    </div>

    <ul class="contact">
      <li class="contact-item">
        <svg class="contact-icon" viewBox="0 0 20 30" aria-label="Phone">
          <rect x="4" y="2" width="12" height="26" rx="2" fill="none" stroke="#fff" stroke-width="2"/>
          <rect x="7" y="5" width="6" height="7" fill="#fff"/>
          <g fill="#fff">
            <rect x="6.5" y="15" width="2" height="2"/><rect x="9" y="15" width="2" height="2"/><rect x="11.5" y="15" width="2" height="2"/>
            <rect x="6.5" y="18.5" width="2" height="2"/><rect x="9" y="18.5" width="2" height="2"/><rect x="11.5" y="18.5" width="2" height="2"/>
            <rect x="6.5" y="22" width="2" height="2"/><rect x="9" y="22" width="2" height="2"/><rect x="11.5" y="22" width="2" height="2"/>
          </g>
        </svg>
        <span>+00 (0) 000 000 0000</span>
      </li>
      <li class="contact-item">
        <svg class="contact-icon" viewBox="0 0 20 30" aria-label="Email">
          <rect x="1" y="10" width="18" height="12" fill="#fff"/>
          <polyline points="1,10 10,17 19,10" fill="none" stroke="#0b2a80" stroke-width="1.5"/>
        </svg>
        <span>yourmail@yourdomain.com</span>
      </li>
    </ul>
  </section>
</div>
</body>
</html>
```